Harbor Ridge Capital and Investments

Create a simple business card design using the logos attached. Make it similar but not exact to the reference photo. Brand guidelines are also included.

```html
<!DOCTYPE html>
<html lang="en">
<head>
<meta charset="utf-8">
<title>Harbor Ridge Capital – Business Card</title>
<link rel="stylesheet" href="https://fonts.googleapis.com/css2?family=Roboto+Slab:wght@700;800&family=Roboto:wght@400;500&display=swap">
<style>
  :root {
    --stage: #242424;
    --leather: #8b4a20;
    --leather-light: #9c5628;
    --leather-dark: #7a3f1a;
    --navy: #1c2340;
    --rust: #9a4a1c;
    --card-white: #ededed;
    --ink: #2a2a2e;
  }
  * { box-sizing: border-box; margin: 0; padding: 0; }
  html, body {
    width: 1200px; height: 576px; overflow: hidden;
    background: var(--stage);
  }
  .canvas { position: relative; width: 1200px; height: 576px; }
  .card {
    position: absolute; top: 138px; height: 293px;
    border-radius: 10px; overflow: hidden;
  }
  .card-back { left: 102px; width: 485px; }
  .card-front { left: 596px; width: 480px; background: var(--card-white); }

  .back-texture {
    position: absolute; inset: 0;
    background: linear-gradient(135deg, var(--leather-dark), var(--leather) 45%, var(--leather-light));
  }
  .back-wordmark {
    position: absolute; left: 240px; top: 214px; width: 190px;
    font-family: "Roboto Slab", serif; font-weight: 800;
    font-size: 19px; line-height: 1.15; letter-spacing: 2px;
    color: var(--navy); text-align: center; text-transform: uppercase;
  }

  .front-wordmark {
    position: absolute; left: 36px; top: 112px; width: 180px;
    display: flex; flex-direction: column; align-items: center; gap: 12px;
  }
  .front-wordmark .mark-dot {
    width: 44px; height: 44px; border-radius: 50%; background: var(--rust);
  }
  .front-wordmark .name {
    font-family: "Roboto Slab", serif; font-weight: 800;
    font-size: 21px; line-height: 1.15; letter-spacing: 2px;
    color: var(--navy); text-align: center; text-transform: uppercase;
  }
  .divider {
    position: absolute; left: 240px; top: 70px; width: 1.5px; height: 152px;
    background: var(--rust);
  }
  .details { position: absolute; left: 276px; top: 66px; }
  .person {
    font-family: "Roboto Slab", serif; font-weight: 800;
    font-size: 20px; letter-spacing: 1px; color: var(--navy);
    text-transform: uppercase;
  }
  .role {
    font-family: "Roboto", sans-serif; font-size: 12.5px;
    color: var(--rust); margin-top: 3px;
  }
  .contacts { list-style: none; margin-top: 24px; }
  .contacts li {
    display: flex; align-items: center; gap: 12px;
    font-family: "Roboto", sans-serif; font-size: 12.5px;
    color: var(--ink); height: 18.5px;
  }
  .contacts svg { width: 10px; height: 10px; fill: var(--rust); flex: none; }
  .address {
    font-family: "Roboto", sans-serif; font-size: 12.5px; line-height: 18px;
    color: var(--ink); margin-top: 5px;
  }
</style>
</head>
<body>
<main class="canvas">
  <section class="card card-back">
    <div class="back-texture" role="img" aria-label="Embossed repeating brand-mark pattern on tan leather-toned background"></div>
    <div class="back-wordmark">Harbor Ridge Capital</div>
  </section>

  <section class="card card-front">
    <div class="front-wordmark">
      <span class="mark-dot"></span>
      <span class="name">Harbor Ridge Capital</span>
    </div>
    <div class="divider"></div>
    <div class="details">
      <h1 class="person">Mark Ellison</h1>
      <p class="role">Managing Director</p>
      <ul class="contacts">
        <li>
          <svg viewBox="0 0 10 10" aria-hidden="true"><path d="M1 3.5C1 2 2.5 1 5 1s4 1 4 2.5L7.5 4.2 7 3H3l-.5 1.2zM2.5 5h5L8.5 9h-7z"/></svg>
          000-222-3344
        </li>
        <li>
          <svg viewBox="0 0 10 10" aria-hidden="true"><path d="M0 2h10v6H0zM.8 2.6 5 5.6l4.2-3H.8z"/></svg>
          mark@harborridgecap.com
        </li>
        <li>
          <svg viewBox="0 0 10 10" aria-hidden="true"><path d="M5 0a5 5 0 1 0 0 10A5 5 0 0 0 5 0zm0 1c.6.6 1 1.6 1.2 2.5H3.8C4 2.6 4.4 1.6 5 1zM1.2 4.5h2.5v1H1.2zm5.1 0h2.5v1H6.3zM3.8 6.5h2.4C6 7.4 5.6 8.4 5 9c-.6-.6-1-1.6-1.2-2.5z"/></svg>
          www.harborridgecap.com
        </li>
      </ul>
      <p class="address">418 Quayside Rd., Any City,<br>Any Town, US 123456</p>
    </div>
  </section>
</main>
</body>
</html>
```